Product Label Design

Need a product design for our Epsom salt product, needs to have a luxurious simple feel to it. The picture attached is our brand and wordage on it, the bag we think should be a stand up bag that should be offwhite/creme color. The other picture are products that we like. We updated the packaging to be a Kraft tube box, please see the attached photo for dimensions.

```html
<!DOCTYPE html>
<html lang="en">
<head>
<meta charset="utf-8">
<title>Saltmere Recovery Bath Salts – Pouch Front</title>
<link rel="stylesheet" href="https://fonts.googleapis.com/css2?family=Bodoni+Moda:wght@400&family=Montserrat:wght@400&family=Questrial&display=swap">
<style>
  :root {
    --backdrop: #e4ddd2;
    --pouch: #efe6d4;
    --pouch-seal: #e8dec9;
    --seal-line: #d9cdb5;
    --gold: #8f7040;
    --gold-soft: #a88a55;
    --ink: #6d5835;
  }
  html, body {
    margin: 0;
    padding: 0;
    width: 1200px;
    height: 933px;
    overflow: hidden;
    background: var(--backdrop);
  }
  .canvas {
    position: relative;
    width: 1200px;
    height: 933px;
  }
  .pouch {
    position: absolute;
    left: 346px;
    top: 93px;
    width: 496px;
    height: 750px;
    background: var(--pouch);
    border-radius: 4px;
    box-shadow: 0 6px 18px rgba(90, 70, 40, 0.12);
    text-align: center;
  }
  .pouch__seal {
    position: absolute;
    left: 0;
    top: 0;
    width: 100%;
    height: 82px;
    background: repeating-linear-gradient(
      to bottom,
      var(--pouch-seal) 0 3px,
      var(--seal-line) 3px 4px
    );
    border-radius: 4px 4px 0 0;
  }
  .pouch__side {
    position: absolute;
    top: 82px;
    bottom: 0;
    width: 26px;
    background: repeating-linear-gradient(
      to right,
      var(--pouch-seal) 0 3px,
      var(--seal-line) 3px 4px
    );
    opacity: 0.6;
  }
  .pouch__side--left { left: 0; }
  .pouch__side--right { right: 0; }
  .brand-name {
    position: absolute;
    left: 0;
    right: 0;
    top: 198px;
    margin: 0;
    font-family: "Bodoni Moda", serif;
    font-weight: 400;
    font-size: 72px;
    line-height: 1;
    letter-spacing: -0.01em;
    color: var(--gold);
  }
  .tagline {
    position: absolute;
    left: 0;
    right: 0;
    top: 283px;
    margin: 0;
    font-family: "Montserrat", sans-serif;
    font-size: 14px;
    letter-spacing: 0.42em;
    color: var(--ink);
  }
  .wave-mark {
    position: absolute;
    left: 216px;
    top: 350px;
    width: 84px;
    height: 32px;
    border-radius: 16px;
    background: linear-gradient(90deg, rgba(168,138,85,0.15), rgba(168,138,85,0.45), rgba(168,138,85,0.15));
  }
  .variant {
    position: absolute;
    left: 0;
    right: 0;
    top: 407px;
    margin: 0;
    font-family: "Bodoni Moda", serif;
    font-size: 30px;
    letter-spacing: -0.01em;
    color: var(--ink);
  }
  .ingredients {
    position: absolute;
    left: 0;
    right: 0;
    top: 454px;
    margin: 0;
    padding: 0;
    list-style: none;
    font-family: "Questrial", sans-serif;
    font-size: 18px;
    line-height: 23px;
    color: var(--gold-soft);
  }
  .net-weight {
    position: absolute;
    left: 0;
    right: 0;
    top: 617px;
    margin: 0;
    font-family: "Questrial", sans-serif;
    font-size: 18px;
    color: var(--ink);
  }
</style>
</head>
<body>
  <main class="canvas">
    <section class="pouch">
      <div class="pouch__seal"></div>
      <div class="pouch__side pouch__side--left"></div>
      <div class="pouch__side pouch__side--right"></div>

      <h1 class="brand-name">SALTMERE</h1>
      <p class="tagline">PREMIUM BATH SALTS</p>

      <div class="wave-mark" role="img" aria-label="Small line ornament of a breaking ocean wave"></div>

      <h2 class="variant">RECOVERY</h2>
      <ul class="ingredients">
        <li>magnesium flakes</li>
        <li>arnica</li>
        <li>eucalyptus</li>
      </ul>

      <p class="net-weight">NET WT. 4 OZ (113)</p>
    </section>
  </main>
</body>
</html>
```